Bref créative
Business Cards and Stationary for Conference App Company
Kalvornet
Modern
Lars Henrik Dalsgaard
Partner
Solbærvej 254
DK-4170 Nørrebjerg
lhd@kalvornet.example
kalvornet.example

```html
<!DOCTYPE html>
<html lang="en">
<head>
<meta charset="utf-8">
<title>Kalvornet business card</title>
<link rel="stylesheet" href="https://fonts.googleapis.com/css2?family=Ubuntu:ital,wght@0,400;0,500;1,400&display=swap">
<style>
  :root {
    --bg: #e4e5e6;
    --card-white: #ffffff;
    --slate: #8a8c8e;
    --slate-dark: #6d6f71;
    --orange: #f5a623;
    --ink-light: #ffffff;
    --ink-grey: #7a7c7e;
  }
  * { box-sizing: border-box; margin: 0; padding: 0; }
  html, body {
    width: 1200px; height: 842px; overflow: hidden;
    background: var(--bg);
    font-family: "Ubuntu", Arial, sans-serif;
  }
  .stage {
    width: 1200px; height: 842px;
    display: flex; align-items: center; justify-content: center; gap: 50px;
  }
  .card {
    width: 540px; height: 309px; position: relative; overflow: hidden;
    box-shadow: 0 6px 18px rgba(0,0,0,0.18);
  }
  .card-front { background: var(--card-white); }
  .brand {
    position: absolute; left: 34px; top: 32px;
    display: flex; align-items: center; gap: 10px;
  }
  .brand-mark { width: 30px; height: 30px; background: var(--slate-dark); }
  .brand-name { font-size: 38px; font-weight: 500; color: var(--slate-dark); line-height: 1; }
  .tagline {
    position: absolute; left: 74px; top: 72px;
    font-size: 14px; color: var(--ink-grey); letter-spacing: 0.3px;
  }
  .info-block {
    position: absolute; left: 0; right: 0; top: 112px; bottom: 34px;
    background: var(--slate);
  }
  .person {
    position: absolute; left: 0; top: 0; width: 290px; height: 58px;
    background: var(--orange); padding: 11px 0 0 34px; color: var(--ink-light);
  }
  .person-name { font-size: 15px; font-weight: 500; }
  .person-title { font-size: 12px; margin-top: 4px; }
  .divider {
    position: absolute; left: 290px; top: 0; bottom: 0; width: 4px; background: var(--card-white);
  }
  .address {
    position: absolute; left: 34px; top: 74px; color: var(--ink-light);
    font-size: 12px; line-height: 1.6;
  }
  .contacts {
    position: absolute; left: 314px; top: 66px; list-style: none;
    color: var(--ink-light); font-size: 12px;
  }
  .contacts li { display: flex; align-items: center; gap: 8px; height: 22px; }
  .contacts svg { width: 14px; height: 14px; flex: none; }
  .card-back { background: var(--slate); }
  .back-brand {
    position: absolute; left: 44px; top: 70px;
    display: flex; align-items: center; gap: 16px;
  }
  .back-mark { width: 70px; height: 70px; background: var(--card-white); }
  .back-name { font-size: 56px; font-weight: 500; color: var(--card-white); line-height: 1; }
  .back-web {
    position: absolute; right: 34px; bottom: 40px;
    font-size: 17px; font-style: italic; letter-spacing: 2px; color: var(--card-white);
  }
</style>
</head>
<body>
<main class="stage">
  <section class="card card-front">
    <div class="brand">
      <span class="brand-mark"></span>
      <span class="brand-name">Kalvornet</span>
    </div>
    <p class="tagline">Your Meeting Rethought</p>
    <div class="info-block">
      <div class="person">
        <p class="person-name">Lars Henrik Dalsgaard</p>
        <p class="person-title">Partner</p>
      </div>
      <div class="divider"></div>
      <p class="address">Solbærvej 254<br>DK-4170 Nørrebjerg</p>
      <ul class="contacts">
        <li>
          <svg viewBox="0 0 16 16"><circle cx="8" cy="8" r="8" fill="#fff"/><path d="M5 4.5l1.6-.3 1 2.2-1 .8a5 5 0 0 0 2.2 2.2l.8-1 2.2 1-.3 1.6c-3.5.3-6.8-3-6.5-6.5z" fill="#8a8c8e"/></svg>
          <span>45 20481736</span>
        </li>
        <li>
          <svg viewBox="0 0 16 16"><circle cx="8" cy="8" r="8" fill="#fff"/><rect x="4" y="5" width="8" height="6" fill="none" stroke="#8a8c8e" stroke-width="1.2"/><path d="M4 5l4 3.2L12 5" fill="none" stroke="#8a8c8e" stroke-width="1.2"/></svg>
          <span>lhd@kalvornet.example</span>
        </li>
        <li>
          <svg viewBox="0 0 16 16"><circle cx="8" cy="8" r="8" fill="#fff"/><circle cx="8" cy="8" r="4.2" fill="none" stroke="#8a8c8e" stroke-width="1.1"/><path d="M3.8 8h8.4M8 3.8c-2 2.4-2 6 0 8.4M8 3.8c2 2.4 2 6 0 8.4" fill="none" stroke="#8a8c8e" stroke-width="1"/></svg>
          <span>www.kalvornet.example</span>
        </li>
      </ul>
    </div>
  </section>

  <section class="card card-back">
    <div class="back-brand">
      <span class="back-mark"></span>
      <span class="back-name">Kalvornet</span>
    </div>
    <p class="back-web">www.kalvornet.example</p>
  </section>
</main>
</body>
</html>
```